Process Roadmap for Interior Design Firm

We are looking to ramp up the design appeal of our current process roadmap to be very visually interesting, while staying informative and descriptive about our process.

Target Market(s)

In-house Clients

Industry/Entity Type

Interior Design Firm focused on sustainable and holistic design.

Other font styles liked:
• raleway

Requirements
Must have
• 1.) it would be nice if the graphic provided a more clear indication of the “journey” from one step to the next, so that there was a clear sense of the progression (such that we are directing the viewer) 2.). We would want it to fit on an 8.5”x11” page (the page could be horizontal when we have the Calm Compass formatted out with the testimonials) (in addition to the testimonials, we may also want to have the detailed descriptions of each step of the process presented below the graphic, so that the graphic is cleaner) 3.) ideally the graphic is clear and simple enough to also be used on our Bi-Weekly Client Updates, which will be typed updates for clients re their project budgets, schedule and scope. The Calm Compass graphic (without all the testimonials) would be at the end of the update, and would fit on the page horizontally at the bottom, perhaps in a space which is 7.5”w x 4”h or so.
Should not have
• bold or bright colors. Natural neutrals are preferred, such as the ones featured on the provided graphic.

```html
<!DOCTYPE html>
<html lang="en">
<head>
<meta charset="utf-8">
<title>Design Process Roadmap</title>
<link href="https://fonts.googleapis.com/css2?family=Raleway:wght@400;500;700&display=swap" rel="stylesheet">
<style>
  :root {
    --khaki: #bdb088;
    --walnut: #9b6e4e;
    --tan: #b39274;
    --copper: #ba8460;
    --ink: #9a6a4b;
    --white: #ffffff;
  }
  html, body { margin: 0; padding: 0; overflow: hidden; }
  body { width: 1200px; height: 720px; background: var(--white); font-family: "Raleway", sans-serif; }
  .roadmap { position: relative; width: 1200px; height: 720px; overflow: hidden; }
  .roadmap svg { position: absolute; left: 0; top: 0; }
  .step-label {
    position: absolute; transform: translate(-50%, -50%);
    color: var(--white); font-weight: 700; font-size: 24px; letter-spacing: 0.2px;
    white-space: nowrap; text-shadow: 0 1px 2px rgba(80,55,35,0.35);
  }
  .step-note {
    position: absolute; transform: translateX(-50%); text-align: center;
    color: var(--ink); font-size: 14px; line-height: 16.6px; font-weight: 400;
  }
  .step-note p { margin: 0 0 3px; }
</style>
</head>
<body>
<main class="roadmap">
  <svg width="1200" height="720" viewBox="0 0 1200 720" xmlns="http://www.w3.org/2000/svg">
    <defs>
      <radialGradient id="dial" cx="50%" cy="40%" r="60%">
        <stop offset="0" stop-color="#ffffff"/>
        <stop offset="1" stop-color="#e4e4e4"/>
      </radialGradient>
    </defs>

    <!-- rule lines -->
    <g stroke-width="3" stroke-linecap="round">
      <line x1="111" y1="73" x2="277" y2="73" stroke="var(--khaki)"/>
      <line x1="317" y1="71" x2="483" y2="71" stroke="var(--walnut)"/>
      <line x1="530" y1="49" x2="734" y2="49" stroke="var(--tan)"/>
      <line x1="774" y1="73" x2="979" y2="73" stroke="var(--khaki)"/>
      <line x1="224" y1="648" x2="437" y2="648" stroke="var(--copper)"/>
      <line x1="506" y1="640" x2="719" y2="640" stroke="var(--khaki)"/>
      <line x1="777" y1="659" x2="990" y2="659" stroke="var(--tan)"/>
    </g>

    <!-- client figures -->
    <g class="clients" fill="var(--khaki)">
      <circle cx="54" cy="213" r="9"/>
      <path d="M42 243 v-13 q0-8 12-8 q12 0 12 8 v13 z"/>
      <circle cx="92" cy="213" r="9"/>
      <path d="M80 243 v-13 q0-8 12-8 q12 0 12 8 v13 z"/>
    </g>

    <!-- top row arrows -->
    <path class="arrow-listening" fill="var(--khaki)" d="M128 209 H283 V188 L356 230 L283 272 V251 H128 Z"/>
    <path class="arrow-visioning" fill="var(--walnut)" d="M339 209 H502 V188 L574 230 L502 272 V251 H339 L376 230 Z"/>
    <path class="arrow-planning" fill="var(--tan)" d="M558 209 H726 V188 L798 230 L726 272 V251 H558 L594 230 Z"/>
    <path class="arrow-designing" fill="var(--khaki)" d="M782 209 H929 C1010 209 1058 260 1064 332 L1084 332 L1045 404 L1001 332 L1021 332 C1014 285 980 251 929 251 H782 L818 230 Z"/>

    <!-- bottom row arrows -->
    <path class="arrow-managing" fill="var(--tan)" d="M1021 387 L1045 421 L1065 387 C1060 480 1010 541 927 541 H758 V561 L685 520 L758 478 V499 H927 C990 499 1018 450 1021 387 Z"/>
    <path class="arrow-installing" fill="var(--khaki)" d="M702 499 H509 V478 L436 520 L509 561 V541 H702 L666 520 Z"/>
    <path class="arrow-completing" fill="var(--copper)" d="M453 499 H210 V478 L138 520 L210 561 V541 H453 L417 520 Z"/>

    <!-- home -->
    <g class="home" fill="var(--copper)">
      <path d="M42 518 L82 472 L97 489 V472 H106 V499 L120 515 V520 H114 V543 H48 V520 H42 Z"/>
      <g fill="var(--white)">
        <rect x="71" y="505" width="8" height="8"/><rect x="83" y="505" width="8" height="8"/>
        <rect x="71" y="517" width="8" height="8"/><rect x="83" y="517" width="8" height="8"/>
      </g>
    </g>

    <!-- top dials -->
    <g class="dial">
      <path fill="var(--khaki)" d="M213 251 L233 272 H193 Z"/>
      <circle cx="213" cy="312" r="45" fill="var(--khaki)"/>
      <circle cx="213" cy="312" r="34" fill="url(#dial)"/>
      <g fill="none" stroke="var(--khaki)" stroke-width="3" stroke-linecap="round">
        <path d="M195 322 c-6-4-6-18 1-22 c8-5 15 2 12 10 c-2 5-6 6-6 12 c0 5-6 6-7 0"/>
        <path d="M212 305 l8 3 M212 312 h8 M212 319 l8-3"/>
      </g>
      <g fill="var(--khaki)"><circle cx="231" cy="307" r="5"/><path d="M223 326 v-8 q0-5 8-5 q8 0 8 5 v8 z"/></g>
    </g>
    <g class="dial">
      <path fill="var(--walnut)" d="M432 251 L452 272 H412 Z"/>
      <circle cx="432" cy="312" r="45" fill="var(--walnut)"/>
      <circle cx="432" cy="312" r="34" fill="url(#dial)"/>
      <path fill="var(--walnut)" d="M407 313 L432 292 L445 303 V290 H450 V307 L457 313 H452 V330 H412 V313 Z"/>
      <ellipse cx="432" cy="313" rx="15" ry="8" fill="var(--white)"/>
      <circle cx="432" cy="313" r="5" fill="var(--walnut)"/>
    </g>
    <g class="dial">
      <path fill="var(--tan)" d="M665 251 L685 272 H645 Z"/>
      <circle cx="665" cy="312" r="45" fill="var(--tan)"/>
      <circle cx="665" cy="312" r="34" fill="url(#dial)"/>
      <rect x="647" y="294" width="36" height="40" rx="4" fill="var(--tan)"/>
      <rect x="657" y="289" width="16" height="8" rx="2" fill="var(--tan)"/>
      <g stroke="var(--white)" stroke-width="2.5" fill="none" stroke-linecap="round">
        <path d="M653 305 h10 M653 314 h10 M653 323 h10"/>
        <path d="M667 305 l3 3 l7-7 M667 314 l3 3 l7-7 M667 323 l3 3 l7-7"/>
      </g>
    </g>
    <g class="dial">
      <path fill="var(--khaki)" d="M905 251 L925 272 H885 Z"/>
      <circle cx="905" cy="312" r="45" fill="var(--khaki)"/>
      <circle cx="905" cy="312" r="34" fill="url(#dial)"/>
      <path d="M893 320 L930 304" stroke="var(--khaki)" stroke-width="5" stroke-linecap="round"/>
      <ellipse cx="889" cy="322" rx="6" ry="4" fill="var(--khaki)"/>
      <path d="M887 318 c-4-8 0-14 6-16" stroke="var(--khaki)" stroke-width="2" fill="none"/>
    </g>

    <!-- bottom dials -->
    <g class="dial">
      <path fill="var(--copper)" d="M325 498 L345 477 H305 Z"/>
      <circle cx="325" cy="439" r="45" fill="var(--copper)"/>
      <circle cx="325" cy="439" r="34" fill="url(#dial)"/>
      <path fill="var(--copper)" d="M303 440 L325 421 L336 430 V420 H341 V434 L347 440 H342 V459 H308 V440 Z"/>
      <g fill="var(--white)"><rect x="320" y="440" width="4" height="4"/><rect x="326" y="440" width="4" height="4"/><rect x="320" y="446" width="4" height="4"/><rect x="326" y="446" width="4" height="4"/></g>
      <path fill="var(--copper)" d="M312 416 l2 6 l6 2 l-6 2 l-2 6 l-2-6 l-6-2 l6-2 z M344 425 l1.5 5 l5 1.5 l-5 1.5 l-1.5 5 l-1.5-5 l-5-1.5 l5-1.5 z"/>
    </g>
    <g class="dial">
      <path fill="var(--khaki)" d="M583 498 L603 477 H563 Z"/>
      <circle cx="583" cy="438" r="45" fill="var(--khaki)"/>
      <circle cx="583" cy="438" r="34" fill="url(#dial)"/>
      <rect x="565" y="419" width="13" height="16" fill="var(--khaki)"/>
      <circle cx="595" cy="427" r="6" fill="var(--khaki)"/>
      <path fill="var(--khaki)" d="M578 440 h10 v4 c6 3 7 9 4 22 h-14 c-3-13-2-19 0-22 z"/>
    </g>
    <g class="dial">
      <path fill="var(--tan)" d="M835 498 L855 477 H815 Z"/>
      <circle cx="835" cy="438" r="45" fill="var(--tan)"/>
      <circle cx="835" cy="438" r="34" fill="url(#dial)"/>
      <g fill="var(--tan)">
        <circle cx="836" cy="420" r="5"/><path d="M829 434 v-6 q0-4 7-4 q7 0 7 4 v6 z"/>
        <circle cx="818" cy="439" r="5"/><path d="M811 453 v-6 q0-4 7-4 q7 0 7 4 v6 z"/>
        <circle cx="853" cy="439" r="5"/><path d="M846 453 v-6 q0-4 7-4 q7 0 7 4 v6 z"/>
      </g>
      <g fill="none" stroke="var(--tan)" stroke-width="1.5">
        <path d="M818 430 q2-8 10-11 M845 419 q7 3 9 11 M825 457 q10 5 22 0"/>
      </g>
    </g>
  </svg>

  <div class="step-label" style="left:214px; top:230px;">Listening</div>
  <div class="step-label" style="left:440px; top:230px;">Visioning</div>
  <div class="step-label" style="left:656px; top:230px;">Planning</div>
  <div class="step-label" style="left:890px; top:230px;">Designing</div>
  <div class="step-label" style="left:875px; top:519px;">Managing</div>
  <div class="step-label" style="left:580px; top:519px;">Installing</div>
  <div class="step-label" style="left:333px; top:519px;">Completing</div>

  <div class="step-note" style="left:200px; top:90px; width:170px;">
    <p>Listen to our clients, their land, and their home</p>
    <p>Identifying their needs, challenges, wishes, and dreams.</p>
  </div>
  <div class="step-note" style="left:410px; top:78px; width:170px;">
    <p>Facilitating a guided visioning process to clarify the deepest intention, true purpose, and highest potential for their home and their future within it</p>
  </div>
  <div class="step-note" style="left:632px; top:59px; width:200px;">
    <p>Turning our client’s vision into a clearly defined scope, budget, and timeline.</p>
    <p>Mapping out the steps for making their dream a reality</p>
    <p>Setting a meeting schedule from start to finish</p>
  </div>
  <div class="step-note" style="left:877px; top:84px; width:200px;">
    <p>Following the schedule through the design phases from initial design concepts, technical drawing and details, and the selection of all finishes, fixture, and surnishings.</p>
  </div>
  <div class="step-note" style="left:330px; top:550px; width:230px;">
    <p>Finding any issue or defects</p>
    <p>Follow up on all remaining items.</p>
    <p>Completing the final finishing touches to our client’s full and total satisfaction</p>
  </div>
  <div class="step-note" style="left:612px; top:548px; width:210px;">
    <p>Overseeing the inspection, installation, and arrangement of all furnishings, lighting, artwork, and decorative items</p>
  </div>
  <div class="step-note" style="left:883px; top:553px; width:240px;">
    <p>Coordinating with clients, builders, architects, and vendors to ensure that the design is executed with excellence, and the construction and furnishing are on-time and on-budget.</p>
  </div>
</main>
</body>
</html>
```